Trade Show booth design

I need the following designs for my trade booth:
1. backboard design 3m Wx2mH
2. Tressle table, tablecloth front panel design 1800W x 740mmH
3. Pop-up banner. I have included our logos and some design content ideas:
Headline:
"Cleaner Classrooms. Safer Schools."
Subheadline:
"Specialist Cleaning Solutions for Education Facilities"
Key Points to Grab Attention:
Healthy Environments: Create hygienic, safe learning spaces for students and staff with our expert cleaning services.
Tailored to Your Needs: Custom cleaning plans for classrooms, labs, libraries, and sports facilities.
Affordable Excellence: Premium results without premium costs – tailored plans mean you only pay for what you need.
Safety First: All staff are trained, highly vetted, and hold current Working with Children Checks (WWCC).
Eco-Conscious Cleaning: Using non-toxic, eco-friendly products certified for health and safety.
What Schools Really Need:
Reliability: Consistent, high-quality cleaning from a trusted provider.
Cost-Effectiveness: Solutions that fit tight budgets while maintaining high standards.
Expertise: Over 30 years of experience in education facility cleaning.
Disinfection Services: Focus on high-touch areas to reduce the spread of germs and ensure peace of mind.
Visual Elements:
Images of bright, clean classrooms, a happy teacher welcoming students, or students collaborating in a spotless library.
Icons representing safety (shield), hygiene (sparkling star), and eco-friendliness (leaf).
Your logo with the tagline: "Trusted by Queensland Schools Since 1995."
Call-to-Action:
"Visit us to discuss your school’s cleaning needs and book a FREE consultation."
Include contact details: Phone: 1300 648 319 | Website: www.vardenmop.com.au
Target Market(s)
Education sector
Industry/Entity Type
Commercial Cleaning
Font styles to use
Other font styles liked:
- Montserrat
Look and feel

```html
<!DOCTYPE html>
<html lang="en">
<head>
<meta charset="utf-8">
<title>Vardenmop – Education Cleaning Backboard</title>
<link rel="stylesheet" href="https://fonts.googleapis.com/css2?family=Montserrat:wght@400;500;600;700;800&display=swap">
<style>
  :root {
    --navy: #1e3c61;
    --sky: #2b8ddc;
    --white: #ffffff;
    --stage: #2a2a2a;
    --photo-grey: #b9bbbd;
    --photo-grey-dark: #8c8f93;
    --photo-wood: #b7ab9b;
    --photo-wood-dark: #6f5a45;
  }
  * { box-sizing: border-box; margin: 0; padding: 0; }
  html, body {
    width: 1200px; height: 1200px; overflow: hidden;
    background: var(--stage);
    font-family: "Montserrat", sans-serif;
  }
  .backboard {
    position: absolute; left: 30px; top: 218px;
    width: 1140px; height: 763px;
    overflow: hidden; background: var(--white);
  }
  .backboard-shapes { position: absolute; inset: 0; width: 100%; height: 100%; }

  .brand {
    position: absolute; left: 38px; top: 40px; width: 440px;
    display: flex; align-items: center; gap: 14px;
  }
  .brand-mark { width: 26px; height: 26px; background: var(--navy); flex: none; }
  .brand-name {
    font-weight: 700; font-size: 58px; letter-spacing: 1px;
    color: var(--navy); line-height: 1;
  }
  .brand-tagline {
    position: absolute; left: 75px; top: 149px;
    font-size: 14.6px; font-weight: 500; color: #1b1b1b; letter-spacing: 0.1px;
  }

  .headline {
    position: absolute; left: 46px; top: 236px;
    color: var(--white); font-weight: 700; font-size: 34px; line-height: 42px;
  }
  .subheadline {
    position: absolute; left: 46px; top: 343px;
    color: var(--white); font-weight: 500; font-size: 26px; line-height: 33px;
  }

  .benefits { position: absolute; left: 0; top: 0; }
  .benefit { position: absolute; width: 150px; text-align: center; }
  .benefit-badge {
    position: absolute; width: 98px; height: 98px; border-radius: 50%;
    background: var(--white); border: 3px solid var(--navy);
    left: 26px; top: 0;
    display: flex; align-items: center; justify-content: center;
  }
  .benefit-badge svg { width: 66px; height: 66px; }
  .benefit-text {
    position: absolute; top: 109px; left: 0; width: 150px;
    color: var(--white); font-size: 12.6px; font-weight: 500; line-height: 15.5px;
  }
  .benefit--experience { left: 50px; top: 449px; }
  .benefit--trust { left: 228px; top: 449px; }
  .benefit--eco { left: 405px; top: 449px; }

  .cta {
    position: absolute; left: 49px; top: 645px;
    color: var(--white); font-size: 19.6px; font-weight: 500; line-height: 22.5px;
  }
  .cta strong { font-weight: 700; }
  .contact {
    position: absolute; left: 48px; top: 695px;
    display: flex; align-items: center; gap: 6px;
    color: var(--white); font-weight: 800; font-size: 26px; letter-spacing: -0.3px;
  }
  .contact svg { width: 20px; height: 20px; flex: none; }
  .contact-divider { margin: 0 6px 0 4px; }
</style>
</head>
<body>
  <main class="backboard">
    <svg class="backboard-shapes" viewBox="0 0 1846 1235" preserveAspectRatio="none" aria-hidden="false">
      <defs>
        <linearGradient id="classroomTone" x1="0" y1="0" x2="1" y2="0">
          <stop offset="0" stop-color="#ffffff"/>
          <stop offset="0.42" stop-color="#ffffff"/>
          <stop offset="0.62" stop-color="#d3d4d5"/>
          <stop offset="1" stop-color="var(--photo-grey-dark)"/>
        </linearGradient>
        <linearGradient id="libraryTone" x1="0" y1="0" x2="0.3" y2="1">
          <stop offset="0" stop-color="#7a4a33"/>
          <stop offset="0.35" stop-color="var(--photo-wood-dark)"/>
          <stop offset="0.55" stop-color="var(--photo-wood)"/>
          <stop offset="1" stop-color="#9f968b"/>
        </linearGradient>
      </defs>

      <g role="img" aria-label="Black and white photo of a teacher at a whiteboard with students in a classroom">
        <rect x="0" y="0" width="1846" height="560" fill="url(#classroomTone)"/>
      </g>

      <g role="img" aria-label="Photo from above of a boy reading a book beside a laptop on a library floor by a bookshelf">
        <polygon points="1610,0 1846,0 1846,1235 1262,1235 940,850 1168,538" fill="url(#libraryTone)"/>
      </g>

      <polygon class="band-sky" points="0,272 929,272 1169,524 942,847 1262,1235 0,1235" fill="var(--sky)"/>
      <polygon class="band-sky-stripe" points="1597,0 1619,0 1181,537 1157,537" fill="var(--sky)"/>
      <polygon class="panel-navy" points="0,297 915,297 1152,545 919,847 0,847" fill="var(--navy)"/>
    </svg>

    <div class="brand">
      <span class="brand-mark"></span>
      <span class="brand-name">Vardenmop</span>
    </div>
    <p class="brand-tagline">TRUSTED BY QUEENSLAND SCHOOLS SINCE 1995</p>

    <h1 class="headline">Creating Cleaner,<br>Safer Learning Environments</h1>
    <p class="subheadline">Specialists in Education<br>Facility Cleaning &amp; Eco-Friendly Services</p>

    <section class="benefits">
      <div class="benefit benefit--experience">
        <div class="benefit-badge">
          <svg viewBox="0 0 64 64" fill="none" stroke="var(--navy)" stroke-width="2.4" stroke-linejoin="round" stroke-linecap="round">
            <path d="M32 6l4 3 5-1 2 5 5 2-1 5 3 4-3 4 1 5-5 2-2 5-5-1-4 3-4-3-5 1-2-5-5-2 1-5-3-4 3-4-1-5 5-2 2-5 5 1z"/>
            <circle cx="32" cy="24" r="10"/>
            <path d="M32 18l1.8 3.8 4 .5-3 2.8.8 4-3.6-2-3.6 2 .8-4-3-2.8 4-.5z"/>
            <path d="M22 40l-7 14 6-1 3 5 6-13M42 40l7 14-6-1-3 5-6-13"/>
          </svg>
        </div>
        <p class="benefit-text">Over 30 years of expertise in commercial cleaning</p>
      </div>

      <div class="benefit benefit--trust">
        <div class="benefit-badge">
          <svg viewBox="0 0 64 64" fill="none" stroke="var(--navy)" stroke-width="2.4" stroke-linejoin="round" stroke-linecap="round">
            <path d="M32 5l10 4v8c0 7-5 11-10 13-5-2-10-6-10-13V9z"/>
            <path d="M27 17l4 4 7-7"/>
            <path d="M4 36l8-8 8 6M60 36l-8-8-8 6"/>
            <path d="M20 34l8-4 6 3 8 8c2 2-1 5-3 3M12 28l-4 12 14 12c2 2 5 0 4-2M39 44c2 2-1 5-3 3l-4-4M36 47c2 2-1 5-3 3l-3-3M33 50c1 2-1 4-3 3"/>
            <path d="M52 28l4 12-8 8"/>
          </svg>
        </div>
        <p class="benefit-text">Trusted by schools, universities, and TAFEs across Queensland</p>
      </div>

      <div class="benefit benefit--eco">
        <div class="benefit-badge">
          <svg viewBox="0 0 64 64" fill="none" stroke="var(--navy)" stroke-width="2.6" stroke-linejoin="round" stroke-linecap="round">
            <circle cx="13" cy="16" r="6" fill="var(--navy)"/>
            <path d="M10 16l2.2 2.2 4-4" stroke="var(--white)" stroke-width="2"/>
            <circle cx="13" cy="33" r="6" fill="var(--navy)"/>
            <path d="M10 33l2.2 2.2 4-4" stroke="var(--white)" stroke-width="2"/>
            <path d="M25 13h22M25 20h22M25 31h12"/>
            <path d="M32 56c0-14 10-22 26-22-1 16-10 22-24 22z" fill="var(--navy)"/>
            <path d="M28 60l16-16" stroke="var(--white)" stroke-width="2"/>
          </svg>
        </div>
        <p class="benefit-text">100% Carbon Neutral and Eco-Certified Services</p>
      </div>
    </section>

    <p class="cta">Visit us to discuss your school’s cleaning needs<br>and book a <strong>FREE</strong> consultation</p>

    <p class="contact">
      <svg viewBox="0 0 24 24" fill="var(--navy)">
        <path d="M6.6 2.5l3 3.2-1.8 2.4c1 2.4 3.6 5 6 6l2.4-1.8 3.2 3-1.6 3.6c-7.6-.4-14.2-7-14.6-14.6z"/>
      </svg>
      <span class="contact-phone">1300 648 319</span>
      <span class="contact-divider">|</span>
      <svg viewBox="0 0 24 24" fill="none" stroke="var(--navy)" stroke-width="1.6">
        <circle cx="12" cy="12" r="9.5"/>
        <ellipse cx="12" cy="12" rx="4.2" ry="9.5"/>
        <path d="M2.5 12h19M4 7h16M4 17h16"/>
      </svg>
      <span class="contact-web">www.vardenmop.com.au</span>
    </p>
  </main>
</body>
</html>
```